political campaign lawn sign - Governor's Council in Massachuesetts

We are looking for a political lawn sign. We are running a campaign for Governor's Council in Massachusetts. This sign will be on the lawn of homes and businesses so people driving by will see it. It needs to be simple and bold. The last name is long so maybe it could say vote for Marty and then Kolbeck will be big a bold on the next line??
We need it to say:
Vote for Martin Kolbeck
Governor's Council.

Target Market(s)

local residents

Industry/Entity Type

Politcal Campaign

Font styles to use
Sans Serif
Other font styles liked:
• not sure what font but a modern looking one such as Helvetica, Arial, Sans Seri, sharp sans..

Colors
0054AA
0677BA
7BADD7
CADEEF
E8F1F8
00AB8E
00BBA5
67D7C9
C6EFE9
E9F9F6
FFF300
FFF600
FEFA6F
FFFEC7
FFFEE8

Requirements
Must have
• My name written out with a Capital D and R but lower case for every other letter so its Marty Kolbeck
Nice to have
• modern font , the Colors of the lawn sign should have Blue, Yellow and White something bold that will stand out
Should not have
• any maps of Massachusetts

```html
<!DOCTYPE html>
<html lang="en">
<head>
<meta charset="utf-8">
<title>Vote for Marty Kolbeck – Governor's Council</title>
<link rel="stylesheet" href="https://fonts.googleapis.com/css2?family=Montserrat:wght@400;500;600;800;900&display=swap">
<style>
  :root {
    --backdrop: #302d2e;
    --sign-navy: #283a6c;
    --sign-yellow: #ffd600;
    --sign-white: #ffffff;
  }
  html, body {
    margin: 0;
    padding: 0;
    width: 1200px;
    height: 1200px;
    overflow: hidden;
    background: var(--backdrop);
  }
  .lawn-sign {
    position: absolute;
    left: 0;
    top: 150px;
    width: 1200px;
    height: 900px;
    display: block;
  }
  .sign-panel { fill: var(--sign-navy); }
  .sign-frame { fill: none; stroke: var(--sign-yellow); stroke-width: 13; }
  .vote-for {
    font-family: "Montserrat", sans-serif;
    font-weight: 400;
    font-size: 82px;
    letter-spacing: 1px;
    fill: var(--sign-yellow);
  }
  .vote-star { fill: var(--sign-yellow); }
  .first-name {
    font-family: "Montserrat", sans-serif;
    font-weight: 500;
    font-size: 250px;
    letter-spacing: -6px;
    fill: var(--sign-white);
  }
  .last-name {
    font-family: "Montserrat", sans-serif;
    font-weight: 900;
    font-size: 196px;
    fill: var(--sign-white);
  }
  .name-rule { stroke: var(--sign-white); stroke-width: 1.5; }
  .office {
    font-family: "Montserrat", sans-serif;
    font-weight: 500;
    font-size: 58px;
    fill: var(--sign-white);
  }
  .web-pill { fill: var(--sign-yellow); }
  .web-address {
    font-family: "Montserrat", sans-serif;
    font-weight: 800;
    font-size: 70px;
    fill: var(--sign-navy);
  }
</style>
</head>
<body>
  <svg class="lawn-sign" viewBox="0 0 1200 900" xmlns="http://www.w3.org/2000/svg">
    <defs>
      <path id="vote-arc" d="M 372 190 A 520 520 0 0 1 828 190" />
    </defs>

    <rect class="sign-panel" x="0" y="0" width="1200" height="900" />
    <rect class="sign-frame" x="30" y="28" width="1140" height="844" />

    <g class="vote-heading">
      <text class="vote-for" text-anchor="middle">
        <textPath href="#vote-arc" startOffset="50%">VOTE FOR</textPath>
      </text>
      <polygon class="vote-star" transform="translate(352 184) rotate(-12)"
        points="0,-15 4.4,-6.1 14.3,-4.6 7.1,2.3 8.8,12.1 0,7.5 -8.8,12.1 -7.1,2.3 -14.3,-4.6 -4.4,-6.1" />
      <polygon class="vote-star" transform="translate(848 184) rotate(12)"
        points="0,-15 4.4,-6.1 14.3,-4.6 7.1,2.3 8.8,12.1 0,7.5 -8.8,12.1 -7.1,2.3 -14.3,-4.6 -4.4,-6.1" />
    </g>

    <text class="first-name" x="600" y="412" text-anchor="middle">Marty</text>
    <text class="last-name" x="154" y="625" textLength="894" lengthAdjust="spacingAndGlyphs">Kolbeck</text>

    <line class="name-rule" x1="151" y1="649" x2="1049" y2="649" />
    <text class="office" x="151" y="710" textLength="898" lengthAdjust="spacing">GOVERNOR'S COUNCIL</text>

    <rect class="web-pill" x="291" y="746" width="622" height="88" rx="14" />
    <text class="web-address" x="316" y="812" textLength="570" lengthAdjust="spacingAndGlyphs">voteformarty.net</text>
  </svg>
</body>
</html>
```